Contemporary Literature/Novel Needs Book Cover Design

This fiction novel is entitled "Before the Tide Turns".
This is a literary fiction piece of work, with the protagonist a female mathematician. The general precis of the novel is her life and her overriding sentimentality that everything on Earth - all life, all memories, all love, all of the events we ever experienced, will all vanish without a trace when the sun dies. I am looking for a classic looking book cover in keeping with the literary feel of the novel, but also something that ties in the mathematics / astronomy of the protagonist's work, and of course the actual title of the book.
The protagonist is a female, the book covers the period of her life from 20 years of age to the late 40's. By "Classic" look I mean: expensive and timeless; something that could have been written 100 years ago, or today.
Please contact me for any further clarifications.
Updates

Reason: Extending deadline to allow for the Easter holiday period as I will b e offline for the next 2 days.

Target Market(s)

Contemporary literature buyers

Industry/Entity Type

Work

Font styles to use
Script

Requirements
Must have
• Cover design that reflects the brief / precis of the novel.
• Author: R.K Fenwick
Should not have
• Images of people

```html
<!DOCTYPE html>
<html lang="en">
<head>
<meta charset="utf-8">
<title>Before the Tide Turns — R.K Fenwick</title>
<link rel="stylesheet" href="https://fonts.googleapis.com/css2?family=Pinyon+Script&family=Bodoni+Moda:wght@500&display=swap">
<style>
  :root {
    --page: #ffffff;
    --cover-ink: #11141a;
    --cover-deep: #07080b;
    --type-light: #ffffff;
    --type-shadow: #000000;
    --emblem-tone: #1c1f26;
    --emblem-glow: #050608;
  }
  * { margin: 0; padding: 0; box-sizing: border-box; }
  html, body {
    width: 1200px;
    height: 808px;
    overflow: hidden;
    background: var(--page);
  }
  .stage {
    position: relative;
    width: 1200px;
    height: 808px;
  }
  .cover {
    position: absolute;
    left: 331px;
    top: 0;
    width: 537px;
    height: 808px;
    background: var(--cover-ink);
    overflow: hidden;
  }
  .author-bar {
    position: absolute;
    top: 22px;
    left: 23px;
    width: 497px;
    height: 56px;
    display: flex;
    align-items: center;
    justify-content: space-between;
  }
  .author-bar .rule {
    flex: 0 0 162px;
    height: 4px;
    background: var(--type-light);
  }
  .author-name {
    flex: 1;
    text-align: center;
    font-family: "Bodoni Moda", serif;
    font-weight: 500;
    font-size: 44px;
    color: var(--type-light);
    letter-spacing: -1px;
    white-space: nowrap;
  }
  .author-name span {
    display: inline-block;
    transform: scaleX(0.62);
  }
  .title {
    position: absolute;
    top: 140px;
    left: 0;
    width: 537px;
    height: 280px;
    font-family: "Pinyon Script", cursive;
    font-weight: 400;
    color: var(--type-light);
    text-shadow: 3px 3px 0 var(--type-shadow), -1px -1px 0 var(--type-shadow);
  }
  .title .line {
    position: absolute;
    white-space: nowrap;
    line-height: 1;
  }
  .title .line-first { left: 112px; top: 0; font-size: 110px; }
  .title .line-article { left: 198px; top: 92px; font-size: 58px; }
  .title .line-noun { left: 290px; top: 78px; font-size: 92px; }
  .title .line-last { left: 130px; top: 160px; font-size: 110px; }
  .emblem {
    position: absolute;
    left: 95px;
    top: 430px;
    width: 350px;
    height: 340px;
    border-radius: 50%;
    background: radial-gradient(circle at 50% 50%, var(--emblem-tone) 0%, var(--emblem-tone) 38%, var(--emblem-glow) 62%, var(--cover-ink) 72%);
  }
</style>
</head>
<body>
  <main class="stage">
    <section class="cover" aria-label="Book cover: Before the Tide Turns by R.K Fenwick">
      <header class="author-bar">
        <span class="rule"></span>
        <p class="author-name"><span>R.K Fenwick</span></p>
        <span class="rule"></span>
      </header>
      <h1 class="title">
        <span class="line line-first">Before</span>
        <span class="line line-article">the</span>
        <span class="line line-noun">Tide</span>
        <span class="line line-last">Turns</span>
      </h1>
      <div class="emblem" role="img" aria-label="Faint engraved sun emblem with radiating rays, glowing softly against the dark cover"></div>
    </section>
  </main>
</body>
</html>
```